We are needed to get an artwork developed for a conference booth across 2 background panels. The design we’d like is of the tree from our existing Meadowlark Studio logo (included). Not wanting a black background.
In addition we’d like the title text
COMMUNITY RECOVERY
COMMUNITY RESILIENCE
A set of national principles
A community of practice
How can we shape the future together?

We are also wanting to have the following text in the roots of the tree.
- Understand the context
- Recognise complexity
- Use community-led approaches
- Coordinate all activities
- Communicate effectively
- Recognise and build capacity

Important – Artwork Requirements
Create 2 conference Digital Print Panels 985mmW x 2347mmH. The conference panels will be put together with a 5mm gap avoid small text in this area.
Print-ready artwork files are to be scaled at correct dimensions.
All artwork must be submitted no larger than 50% scale. Do not supply artwork files over 300MB for large images – Scaling to 50% @ 300 DPI is preferred.
No bleed required for panel prints.
All fonts must be outlined.
Overprint to be turned OFF.
Flatten all transparencies.
Supply as one single layer.
Embed all links.
PDF file submission
Please supply artwork to the exact specifications (dimension, text and images) and high resolution print-ready files.

```html
<!DOCTYPE html>
<html lang="en">
<head>
<meta charset="utf-8">
<title>Community Recovery Community Resilience – Booth Panels</title>
<link href="https://fonts.googleapis.com/css2?family=Saira+Condensed:wght@600;700&family=Poppins:wght@400;500&display=swap" rel="stylesheet">
<style>
  :root {
    --stage: #4d4d4d;
    --forest-deep: #1f3a25;
    --forest-mid: #3f6b3e;
    --forest-light: #5d8a4e;
    --teal-deep: #003a36;
    --teal-mid: #004a44;
    --lime: #8dc63f;
    --white: #ffffff;
  }
  * { margin: 0; padding: 0; box-sizing: border-box; }
  html, body { width: 1200px; height: 1001px; overflow: hidden; }
  body { background: var(--stage); position: relative; font-family: "Poppins", sans-serif; }

  .panel { position: absolute; top: 67px; width: 364px; height: 866px; overflow: hidden; }
  .panel--title { left: 222px;
    background: radial-gradient(ellipse at 50% 35%, var(--forest-mid) 0%, var(--forest-deep) 70%, #162b1b 100%); }
  .panel--principles { left: 614px; background: linear-gradient(180deg, var(--teal-mid) 0%, var(--teal-deep) 100%); }

  .foliage-photo { position: absolute; left: 0; top: 541px; width: 364px; height: 325px;
    background: radial-gradient(ellipse 75% 70% at 50% 55%, var(--forest-light) 0%, #3c6a2e 55%, #2b4d24 100%);
    border-radius: 45% 45% 0 0 / 18% 18% 0 0; }

  .brand { position: absolute; left: 0; width: 100%; top: 56px; text-align: center; color: var(--white); }
  .brand__name { font-family: "Saira Condensed", sans-serif; font-weight: 600; font-size: 24px; line-height: 1;
    display: inline-flex; align-items: center; gap: 8px; }
  .brand__dot { width: 12px; height: 12px; border-radius: 50%; background: var(--white); }
  .brand__tag { font-size: 6px; margin-top: 4px; letter-spacing: 0.2px; }

  .headline { position: absolute; left: 0; width: 100%; text-align: center;
    font-family: "Saira Condensed", sans-serif; font-weight: 700; text-transform: uppercase; line-height: 0.92; font-size: 58px; }
  .headline--recovery { top: 150px; }
  .headline--resilience { top: 276px; }
  .headline .lime { color: var(--lime); }
  .headline .white { color: var(--white); }

  .taglines { position: absolute; left: 0; width: 100%; top: 402px; text-align: center; color: var(--white); font-size: 16.5px; line-height: 1.3; }
  .taglines p + .divider, .divider + p { margin-top: 6px; }
  .divider { display: block; margin: 0 auto; }

  .roots-photo { position: absolute; left: 0; top: 0; width: 364px; height: 253px;
    background: linear-gradient(180deg, #3a5a3a 0%, #4a4236 45%, #3b3228 70%, var(--teal-mid) 100%); }

  .principles { position: absolute; left: 38px; top: 268px; list-style: none; }
  .principle { display: flex; gap: 14px; font-family: "Saira Condensed", sans-serif; font-weight: 600;
    font-size: 34px; line-height: 36px; height: 88px; }
  .principle::before { content: ""; width: 5px; flex: none; height: 68px; margin-top: 2px; background: currentColor; }
  .principle--lime { color: var(--lime); }
  .principle--lime::before { background: var(--white); }
  .principle--white { color: var(--white); }
  .principle--white::before { background: var(--lime); }
</style>
</head>
<body>
  <section class="panel panel--title">
    <div class="foliage-photo" role="img" aria-label="Photograph of a leafy green tree canopy"></div>

    <div class="brand">
      <div class="brand__name"><span class="brand__dot"></span>Meadowlark Studio</div>
      <div class="brand__tag">A space for community recovery practitioners</div>
    </div>

    <h1 class="headline headline--recovery"><span class="white">Community</span><br><span class="lime">Recovery</span></h1>
    <h1 class="headline headline--resilience"><span class="white">Community</span><br><span class="lime">Resilience</span></h1>

    <div class="taglines">
      <p>A set of national principles</p>
      <svg class="divider" width="156" height="8" viewBox="0 0 156 8"><line x1="0" y1="4" x2="72" y2="4" stroke="#fff" stroke-width="1"/><rect x="75" y="1" width="6" height="6" fill="#fff" transform="rotate(45 78 4)"/><line x1="84" y1="4" x2="156" y2="4" stroke="#fff" stroke-width="1"/></svg>
      <p>A community of practice</p>
      <svg class="divider" width="156" height="8" viewBox="0 0 156 8"><line x1="0" y1="4" x2="72" y2="4" stroke="#fff" stroke-width="1"/><rect x="75" y="1" width="6" height="6" fill="#fff" transform="rotate(45 78 4)"/><line x1="84" y1="4" x2="156" y2="4" stroke="#fff" stroke-width="1"/></svg>
      <p>How can we shape<br>the future together?</p>
    </div>
  </section>

  <section class="panel panel--principles">
    <div class="roots-photo" role="img" aria-label="Photograph of a tree trunk with its roots spreading out below"></div>
    <ul class="principles">
      <li class="principle principle--lime"><span>Understand<br>the context</span></li>
      <li class="principle principle--white"><span>Recognise<br>complexity</span></li>
      <li class="principle principle--lime"><span>Use community-led<br>approaches</span></li>
      <li class="principle principle--white"><span>Coordinate<br>all activities</span></li>
      <li class="principle principle--lime"><span>Communicate<br>effectively</span></li>
      <li class="principle principle--white"><span>Recognise<br>and build capacity</span></li>
    </ul>
  </section>
</body>
</html>
```